Redesign Web Page

I am looking for a great re-design and possibly a banner for TwinFlare.us. The site is for an online dating (self-development, online dating) book. The purpose is to drive book sales.

Target Market(s)

Women 18-55

```html
<!DOCTYPE html>
<html lang="en">
<head>
<meta charset="utf-8">
<title>TwinFlare — Online Dating Made Easy</title>
<link rel="stylesheet" href="https://fonts.googleapis.com/css2?family=Questrial&family=Varela+Round&family=Libre+Baskerville:ital@0;1&display=swap">
<style>
:root{
  --page-bg:#f3f1ec;
  --white:#ffffff;
  --pink:#e83d73;
  --pink-soft:#ef6a93;
  --pink-dark:#c4305e;
  --navy:#2f3e52;
  --navy-dark:#293748;
  --blue:#3b8fd6;
  --sky:#3aa0d8;
  --text:#4a4a4a;
  --line:#d9d9d9;
}
*{margin:0;padding:0;box-sizing:border-box}
html,body{width:1027px;height:1200px;overflow:hidden}
body{background:var(--page-bg);font-family:"Questrial",sans-serif;color:var(--text);position:relative}
.page{position:absolute;left:80px;top:0;width:867px;height:1200px;background:var(--white);box-shadow:0 0 6px rgba(0,0,0,.08)}
.abs{position:absolute}
.nowrap{white-space:nowrap}

/* header */
.brand{left:26px;top:30px}
.brand-name{font-family:"Varela Round",sans-serif;font-size:40px;color:var(--navy);letter-spacing:-.5px;line-height:1}
.brand-tag{font-size:15px;color:var(--blue);letter-spacing:1.3px;margin-top:6px}
.social{top:7px;left:752px;display:flex;gap:10px}
.social span{width:29px;height:29px;border-radius:7px;display:block}
.social .s1{background:#4a7fc0}.social .s2{background:#3fb8d6}.social .s3{background:#d94038}

.main-nav{left:275px;top:46px;width:608px;height:42px;background:var(--pink)}
.main-nav a{position:absolute;top:0;height:42px;display:flex;align-items:center;justify-content:center;transform:translateX(-50%);color:var(--white);text-decoration:none;font-size:11px;letter-spacing:1px;text-align:center;line-height:12px;text-transform:uppercase;white-space:nowrap}
.main-nav a.current{left:0;transform:none;width:64px;background:var(--pink-soft)}
.nav-fold{left:867px;top:88px}

.sub-nav{left:0;top:108px;width:867px;height:28px;background:var(--navy)}
.sub-nav .blog{position:absolute;left:0;top:0;width:240px;height:28px;color:var(--white);font-size:11.5px;letter-spacing:.6px;display:flex;align-items:center;padding-left:77px;background:var(--navy-dark);clip-path:polygon(0 0,230px 0,240px 50%,230px 100%,0 100%);white-space:nowrap}
.sub-nav a{position:absolute;top:0;height:28px;display:flex;align-items:center;transform:translateX(-50%);color:var(--white);text-decoration:none;font-size:11px;letter-spacing:.4px;white-space:nowrap}

/* hero */
.hero{left:0;top:136px;width:867px;height:388px;background:radial-gradient(circle at 55% 30%,#fff1c4 0,#e8c58a 12%,#a98a5c 35%,#5e5443 70%,#3c3a33 100%)}
.hero-quote{left:250px;top:162px;width:428px;height:54px;background:rgba(60,60,60,.82);color:var(--white);font-family:"Libre Baskerville",serif;font-style:italic;font-size:17px;letter-spacing:.6px;display:flex;align-items:center;justify-content:center;white-space:nowrap}
.hero-banner{left:78px;top:216px;width:734px;height:56px;background:rgba(59,143,214,.88);color:var(--white);font-size:21px;letter-spacing:1.3px;display:flex;align-items:center;justify-content:center;white-space:nowrap}

/* signup */
.signup{left:0;top:524px;width:867px;height:68px;background:var(--pink)}
.signup h2{position:absolute;left:80px;top:8px;font-weight:400;font-size:22px;line-height:27px;color:var(--white);white-space:nowrap}
.signup .field{position:absolute;top:21px;width:108px;height:27px;background:var(--white)}
.signup .submit{position:absolute;left:659px;top:21px;width:63px;height:27px;background:var(--sky);color:var(--white);font-size:11px;display:flex;align-items:center;justify-content:center}

/* intro */
.book{left:36px;top:669px;width:146px;height:224px;background:linear-gradient(160deg,#f4f4f4,#dcdcdc 60%,#c9c9c9);transform:rotate(-4deg);box-shadow:4px 6px 10px rgba(0,0,0,.25)}
.intro-title{left:226px;top:640px;font-weight:400;font-family:"Libre Baskerville",serif;font-style:italic;font-size:22px;color:var(--pink);white-space:nowrap}
.intro-text{left:238px;top:680px;width:312px;font-size:11px;line-height:18px;color:#555}
.intro-text p{text-indent:10px}

.review{left:587px;top:646px;width:271px;height:71px;background:var(--navy)}
.review-photo{left:0;top:0;width:72px;height:71px;background:linear-gradient(160deg,#7a5a47,#b98c72 50%,#5a4a40)}
.review-name{left:90px;top:10px;color:var(--white);font-size:13.5px;white-space:nowrap}
.review-role{left:90px;top:36px;color:var(--white);font-size:10px;line-height:11px;white-space:nowrap}
.review-tail{left:768px;top:717px}
.review-quote{left:600px;top:752px;width:256px;font-family:"Libre Baskerville",serif;font-style:italic;font-size:11.4px;line-height:15.2px;color:#333}

/* promo */
.promo{left:0;top:949px;width:867px;height:163px;background:linear-gradient(180deg,#e66a8f 0,#e04d7b 55%,#c8406d 100%)}
.promo h3{position:absolute;width:100%;top:52px;text-align:center;font-weight:400;font-size:22px;letter-spacing:2px;color:var(--white)}
.promo .buy{position:absolute;left:355px;top:99px;width:155px;height:41px;border:1px solid rgba(255,255,255,.85);color:var(--white);font-size:13px;letter-spacing:1.3px;display:flex;align-items:center;justify-content:center}

/* footer */
.footer-nav{left:20px;top:1134px;width:826px;height:37px;padding:0 8px;border-top:1px dotted var(--line);border-bottom:1px dotted var(--line);display:flex;align-items:center;justify-content:space-between;font-size:11px;letter-spacing:1.2px;color:#555;white-space:nowrap}
.copyright{left:0;top:1182px;width:867px;text-align:center;font-size:9.5px;letter-spacing:1.5px;color:#555;white-space:nowrap}
</style>
</head>
<body>
<div class="page">
  <header>
    <div class="abs brand">
      <div class="brand-name">twinflare</div>
      <div class="brand-tag nowrap">ONLINE DATING MADE EASY</div>
    </div>
    <div class="abs social" aria-label="Social links"><span class="s1"></span><span class="s2"></span><span class="s3"></span></div>
    <nav class="abs main-nav">
      <a class="current" href="#">Home</a>
      <a href="#" style="left:101px">The<br>Author</a>
      <a href="#" style="left:180px">Fan Fare<br>&amp; Fun</a>
      <a href="#" style="left:278px">Celeb<br>Endorsement</a>
      <a href="#" style="left:372px">Love<br>Stories</a>
      <a href="#" style="left:455px">Products<br>&amp; Services</a>
      <a href="#" style="left:547px">Contact<br>Us</a>
    </nav>
    <svg class="abs nav-fold" width="16" height="8" viewBox="0 0 16 8"><polygon points="0,0 16,0 16,7" fill="#c4305e"/></svg>
    <nav class="abs sub-nav">
      <div class="blog">READ IN OUR BLOG</div>
      <a href="#" style="left:298px">LOVELY TIPS</a>
      <a href="#" style="left:401px">ONLINE TIPS</a>
      <a href="#" style="left:498px">HEALTH TIPS</a>
      <a href="#" style="left:600px">MAKEUP TIPS</a>
      <a href="#" style="left:712px">SEARCH TIPS</a>
      <a href="#" style="left:814px">ENERGY TIPS</a>
    </nav>
  </header>

  <section class="abs hero" role="img" aria-label="Photo of a couple embracing on a beach at sunset with palm trees">
    <div class="abs hero-quote">“Looking for my flame, I found my fire!”</div>
    <div class="abs hero-banner">BECOME THE QUEEN OF ONLINE DATING IN A SKINNY MINUTE</div>
  </section>

  <section class="abs signup">
    <h2>FREE Online<br>Dating Tips</h2>
    <div class="field" style="left:243px"></div>
    <div class="field" style="left:378px"></div>
    <div class="field" style="left:514px"></div>
    <div class="submit">SUBMIT</div>
  </section>

  <div class="abs book" role="img" aria-label="Book cover of the dating guide by Nora Vance with an illustrated woman in a red gown"></div>
  <h1 class="abs intro-title">Lorem Ipsum!</h1>
  <div class="abs intro-text">
    <p>Lorem Ipsum is simply dummy text of the printing and typesetting industry. Lorem Ipsum has been the industry's standard dummy text ever since the 1500s, when an unknown printer took a galley of type and scrambled it to make a type specimen book.</p>
    <p>It has survived not only five centuries, but also the leap into electronic typesetting, remaining essentially unchanged. Lorem Ipsum is simply dummy text of the printing and typesetting industry. Lorem Ipsum has been the industry's standard dummy text</p>
  </div>

  <div class="abs review">
    <div class="abs review-photo" role="img" aria-label="Portrait photo of the reviewer"></div>
    <div class="abs review-name">Claire Hollis</div>
    <div class="abs review-role">author of four #1<br>Daily Ledger Best Sellers</div>
  </div>
  <svg class="abs review-tail" width="44" height="24" viewBox="0 0 44 24"><polygon points="0,0 44,0 0,24" fill="#2f3e52"/></svg>
  <blockquote class="abs review-quote">"Few things are better than a good sit-down chat with a close girl-friend...especially when she knows what she's talking about. Author Nora Vance becomes your newest close girlfriend and she knows what she's talking about. Like a combination of a relationships therapist and a character out of an Emma Brontley novel, Vance entertainingly delivers some pretty serious goods."</blockquote>

  <section class="abs promo" role="img" aria-label="Pink-tinted photo of a couple on a beach with palm trees">
    <h3>NOW AVAILABLE</h3>
    <div class="buy">BUY THE BOOK</div>
  </section>

  <footer>
    <nav class="abs footer-nav">
      <span>HOME</span><span>|</span><span>THE AUTHOR</span><span>|</span><span>FAN FAIR &amp; FUN</span><span>|</span><span>CELEB ENDORSEMENTS</span><span>|</span><span>LOVE STORIES</span><span>|</span><span>PRODUCTS &amp; SERVICES</span><span>|</span><span>CONTACT US</span>
    </nav>
    <div class="abs copyright">COPYRIGHT © 2014 TWIN FLARE ALL RIGHTS RESERVED.</div>
  </footer>
</div>
</body>
</html>
```